Accommodation business card design

We need a business card designed for our long-term accommodation business based in Australia. The business card must match the style of the attached letterhead and logo. The same contact details that are on the letterhead will also go on the card except that the card must list the contact details in the following order:phone, email, home address, ABN.

The card will be printed on .76mm white pvc plastic (same as credit cards), printed both sides and will be silver foil stamped on at least one side (preferably 2 sides) The design template is attached, but please go to www.zt.com.au for more specs.

The only other addition the card will be my name: Malcolm Darby

```html
<!DOCTYPE html>
<html lang="en">
<head>
<meta charset="utf-8">
<title>Kestrel Rentals – Business Card</title>
<link href="https://fonts.googleapis.com/css2?family=Carlito:wght@400;700&display=swap" rel="stylesheet">
<style>
  :root {
    --page-bg: #e6e9ea;
    --card-white: #ffffff;
    --maroon: #5a0b25;
    --rust: #7a2a22;
    --text-red: #8a2b22;
    --emblem-light: #dde3e5;
    --emblem-dark: #6e1a33;
    --on-dark: #ffffff;
  }
  * { margin: 0; padding: 0; box-sizing: border-box; }
  html, body {
    width: 1200px; height: 900px; overflow: hidden;
    background: var(--page-bg);
    font-family: "Carlito", "Calibri", sans-serif;
  }
  .canvas { position: relative; width: 1200px; height: 900px; }

  .card {
    position: absolute; left: 340px;
    width: 520px; height: 328px;
    border-radius: 22px; overflow: hidden;
    box-shadow: 0 6px 18px rgba(0,0,0,0.18);
  }
  .card-art { position: absolute; inset: 0; width: 100%; height: 100%; }

  /* front */
  .card-front { top: 92px; background: var(--card-white); }
  .brand { position: absolute; left: 30px; top: 28px; display: flex; align-items: center; gap: 12px; }
  .brand-square { width: 40px; height: 40px; border-radius: 6px; background: var(--maroon); }
  .brand-name { font-weight: 700; font-size: 26px; color: var(--maroon); letter-spacing: 0.5px; line-height: 1; }
  .holder {
    position: absolute; left: 30px; top: 96px; width: 240px;
    font-size: 21px; font-weight: 400; color: var(--text-red); text-transform: uppercase;
    padding-bottom: 6px; border-bottom: 1px dotted var(--text-red);
  }
  .contacts { position: absolute; left: 30px; top: 140px; list-style: none; font-size: 13px; color: var(--text-red); }
  .contacts li { display: flex; align-items: flex-start; gap: 7px; margin-bottom: 5px; line-height: 1.25; }
  .contacts .icon { flex: none; width: 13px; height: 13px; margin-top: 1px; }
  .contacts .abn { padding-left: 20px; }

  /* back */
  .card-back { top: 480px; background: var(--maroon); }
  .back-name {
    position: absolute; right: 36px; top: 108px;
    color: var(--on-dark); font-weight: 700; font-size: 34px;
    letter-spacing: 0.5px; line-height: 1; white-space: nowrap;
  }
</style>
</head>
<body>
<main class="canvas">

  <section class="card card-front" aria-label="Card front">
    <svg class="card-art" viewBox="0 0 520 328">
      <rect role="img" aria-label="Large house emblem decoration" x="330" y="70" width="160" height="120" rx="10" fill="var(--emblem-light)"/>
      <path d="M190 292 Q330 196 520 202 L520 328 L230 328 Z" fill="var(--rust)"/>
    </svg>

    <div class="brand">
      <span class="brand-square"></span>
      <span class="brand-name">Kestrel Rentals</span>
    </div>

    <h1 class="holder">Malcolm Darby</h1>

    <ul class="contacts">
      <li>
        <svg class="icon" viewBox="0 0 14 14"><circle cx="7" cy="7" r="7" fill="var(--maroon)"/><path d="M7 3.2a2.3 2.3 0 0 0-2.3 2.3C4.7 7.3 7 10.6 7 10.6s2.3-3.3 2.3-5.1A2.3 2.3 0 0 0 7 3.2z" fill="#fff"/></svg>
        <span>PO Box 1180, Harbour Mail Centre<br>QLD 4870</span>
      </li>
      <li>
        <svg class="icon" viewBox="0 0 14 14"><circle cx="7" cy="7" r="7" fill="var(--maroon)"/><path d="M4.6 3.6l1.4-.3.8 1.8-.9.7c.4.9 1.1 1.6 2 2l.7-.9 1.8.8-.3 1.4c-3.3.2-5.7-2.2-5.5-5.5z" fill="#fff"/></svg>
        <span>0400 555 018</span>
      </li>
      <li>
        <svg class="icon" viewBox="0 0 14 14"><circle cx="7" cy="7" r="7" fill="var(--maroon)"/><rect x="3.5" y="4.5" width="7" height="5" fill="#fff"/><path d="M3.5 4.5L7 7.3l3.5-2.8" fill="none" stroke="var(--maroon)" stroke-width="0.8"/></svg>
        <span>malcolm.darby@mailbox.com</span>
      </li>
      <li class="abn">ABN 12 345 678 901</li>
    </ul>
  </section>

  <section class="card card-back" aria-label="Card back">
    <svg class="card-art" viewBox="0 0 520 328">
      <rect role="img" aria-label="Large house emblem decoration" x="40" y="60" width="150" height="125" rx="10" fill="var(--emblem-dark)"/>
      <path d="M0 214 Q190 200 300 328 L0 328 Z" fill="var(--rust)"/>
    </svg>
    <p class="back-name">Kestrel Rentals</p>
  </section>

</main>
</body>
</html>
```